Business Card for Corvane Digital
Corvane Digital
Project: Business Card for Corvane Digital
Business Card for Corvane Digital - Information Technology
Creative Brief
Professional
Dana Holbrook
7312 Ferncliff Drive #210 Larkfield, OR 97419
541-486-3071 ext. 214
dana.holbrook@corvane.example
www.corvane.example
Please incorporate uploaded logo in your design
Logo + Corvane Digital or designs' ideas

```html
<!DOCTYPE html>
<html lang="en">
<head>
<meta charset="utf-8">
<title>Corvane Digital Business Card</title>
<link rel="stylesheet" href="https://fonts.googleapis.com/css2?family=Cardo:wght@400;700&display=swap">
<style>
  :root {
    --stage: #050505;
    --card-light: #3fc3f0;
    --card-mid: #2a86dc;
    --card-deep: #2b3fb6;
    --back-glow: #3a86e6;
    --back-deep: #2b35a8;
    --band: #2a6fd6;
    --band-line: #6fd6fb;
    --wordmark: #152c8c;
    --text: #ffffff;
    --mark: #1d3a9e;
  }
  * { margin: 0; padding: 0; box-sizing: border-box; }
  html, body { width: 1200px; height: 899px; overflow: hidden; background: var(--stage); }
  body { position: relative; font-family: "Cardo", Georgia, serif; color: var(--text); }

  .card { position: absolute; border-radius: 26px; overflow: hidden; }

  .card--front {
    left: 302px; top: 61px; width: 667px; height: 379px;
    background: linear-gradient(125deg, var(--card-light) 0%, var(--card-mid) 48%, var(--card-deep) 100%);
  }
  .front__mark {
    position: absolute; left: 36px; top: 18px; width: 88px; height: 88px;
    border-radius: 50%; background: radial-gradient(circle at 38% 35%, #5a8ee6, var(--mark) 70%);
  }
  .front__name {
    position: absolute; right: 38px; top: 80px; font-size: 30px; line-height: 1;
    text-decoration: underline; text-underline-offset: 5px; text-decoration-thickness: 2px;
  }
  .front__band { position: absolute; left: 0; top: 124px; width: 667px; height: 76px; }
  .front__wordmark {
    position: absolute; left: 0; top: 124px; width: 667px; height: 76px;
    display: flex; align-items: center; justify-content: center;
    font-size: 46px; font-weight: 700; color: var(--wordmark); letter-spacing: 0.5px;
  }
  .contact { position: absolute; left: 27px; top: 222px; list-style: none; font-size: 17px; }
  .contact li { display: flex; height: 25.5px; align-items: center; white-space: nowrap; }
  .contact__label { width: 80px; flex: none; }
  .contact__value { text-decoration: underline; text-underline-offset: 3px; text-decoration-thickness: 1px; }

  .card--back {
    left: 338px; top: 460px; width: 667px; height: 380px;
    background: radial-gradient(ellipse 60% 70% at 50% 35%, var(--back-glow) 0%, var(--back-deep) 100%);
  }
  .back__mark {
    position: absolute; left: 250px; top: 64px; width: 136px; height: 136px;
    border-radius: 50%; background: radial-gradient(circle at 38% 35%, #5a8ee6, var(--mark) 70%);
  }
  .back__wordmark {
    position: absolute; left: 0; width: 100%; top: 216px; text-align: center;
    font-size: 46px; font-weight: 700; color: var(--wordmark); line-height: 1;
  }
  .back__website {
    position: absolute; left: 0; width: 100%; top: 287px; text-align: center; font-size: 24px;
  }
  .back__website span { text-decoration: underline; text-underline-offset: 4px; text-decoration-thickness: 1px; }
</style>
</head>
<body>
  <section class="card card--front">
    <div class="front__mark"></div>
    <div class="front__name">Dana Holbrook</div>
    <svg class="front__band" viewBox="0 0 667 76" aria-hidden="true">
      <rect x="0" y="8" width="667" height="60" fill="var(--band)" opacity="0.85"/>
      <g fill="var(--band-line)">
        <rect x="0" y="14" width="130" height="5"/>
        <rect x="0" y="27" width="120" height="4"/>
        <rect x="0" y="40" width="110" height="4"/>
        <rect x="0" y="53" width="125" height="5"/>
        <rect x="537" y="14" width="130" height="5"/>
        <rect x="557" y="27" width="110" height="4"/>
        <rect x="547" y="40" width="120" height="4"/>
        <rect x="537" y="53" width="130" height="5"/>
      </g>
    </svg>
    <div class="front__wordmark">Corvane Digital</div>
    <ul class="contact">
      <li><span class="contact__label">Address:</span><span class="contact__value">7312 Ferncliff Drive #210 Larkfield, OR 97419</span></li>
      <li><span class="contact__label">Toll Free:</span><span class="contact__value">1-866-(415-2096)</span></li>
      <li><span class="contact__label">Email:</span><span class="contact__value">dana.holbrook@corvane.example</span></li>
      <li><span class="contact__label">Phone:</span><span class="contact__value">541-486-3071 ext. 214</span></li>
      <li><span class="contact__label">Cell:</span><span class="contact__value">541-730-5182</span></li>
    </ul>
  </section>

  <section class="card card--back">
    <div class="back__mark"></div>
    <div class="back__wordmark">Corvane Digital</div>
    <div class="back__website"><span>Website: www.corvane.example</span></div>
  </section>
</body>
</html>
```